SOS! The Bramble cafe is in need of a menu face lift!

We need a standout looking menu for our evolving cafe. Our business has grown greatly from our fresh and changing menu, however the menu (look) itself isn't inspiring and is basic.
I have attached some photos of the business and menus I like the look of.
I am open to other ideas (this is why I need your creative help)
Our menu is currently on an A5 clip board, however we are willing to change it a different size if needed.
Updates

Would love to have it a multi function eg, used as a takeaway menu as well, possibly bi-fold? Added Wednesday, June 8, 2016

Industry/Entity Type

Business

Requirements
Nice to have
• It would be cool to have some old sea/ pirate references?

```html
<!DOCTYPE html>
<html lang="en">
<head>
<meta charset="utf-8">
<title>The Bramble — The Menu</title>
<link rel="stylesheet" href="https://fonts.googleapis.com/css2?family=Playfair+Display:wght@400;700&family=Crimson+Text:ital,wght@0,400;0,600;1,400&family=Lato:wght@400;700&display=swap">
<style>
  :root{
    --navy:#1f3a6e;
    --navy-soft:#3a5487;
    --sky:#a9c1e0;
    --sky-pale:#d3e0f0;
    --paper:#f5f8fc;
    --backdrop:#2a2a2c;
    --price:#8a8f99;
    --kids:#8fa9cc;
    --alert:#8a1c1c;
    --ink:#3d4a60;
  }
  *{box-sizing:border-box;margin:0;padding:0}
  html,body{width:1200px;height:921px;overflow:hidden;background:var(--backdrop)}
  body{position:relative;font-family:"Crimson Text",Georgia,serif;color:var(--ink)}

  .menu{position:absolute;left:255px;top:14px;width:690px;height:892px;background:var(--paper);overflow:hidden}

  /* header */
  .brand{position:absolute;top:10px;left:0;right:0;display:flex;flex-direction:column;align-items:center;gap:6px}
  .brand-dot{width:42px;height:42px;border-radius:50%;background:var(--navy)}
  .brand-name{font-family:"Playfair Display",Georgia,serif;font-size:15px;color:var(--navy);letter-spacing:1px}
  .address{position:absolute;top:98px;left:0;right:0;text-align:center;font-family:"Lato",Arial,sans-serif;font-size:7.5px;color:var(--navy)}
  .title{position:absolute;top:112px;left:0;right:0;text-align:center;font-family:"Playfair Display",Georgia,serif;font-size:58px;letter-spacing:5px;color:var(--navy);line-height:1.3}
  .rule{position:absolute;left:0;right:0;height:4px;background:var(--sky)}
  .rule-top{top:202px}
  .rule-knot{position:absolute;left:337px;top:197px;width:14px;height:14px;border-radius:50%;background:var(--sky)}

  /* sections */
  .section{position:absolute;left:0;right:0;border-bottom:2px solid var(--sky)}
  .breakfast{top:206px;height:270px}
  .lunch{top:476px;height:192px}
  .others{top:668px;height:224px;border-bottom:none}
  .side-label{position:absolute;left:0;top:0;bottom:0;width:83px;border-right:3px double var(--sky);display:flex;justify-content:center;align-items:center;gap:6px;writing-mode:vertical-rl;transform:rotate(180deg)}
  .side-label .main{font-family:"Playfair Display",Georgia,serif;font-size:24px;letter-spacing:3px;color:var(--navy)}
  .side-label .sub{font-family:"Lato",Arial,sans-serif;font-size:8px;letter-spacing:1.5px;color:var(--navy-soft)}
  .side-label .sub.light{color:var(--sky)}

  .col{position:absolute;top:10px;display:flex;flex-direction:column;gap:7px}
  .item{}
  .head{display:flex;justify-content:space-between;align-items:baseline;gap:4px}
  .name{font-size:11.5px;font-weight:600;color:var(--navy);line-height:1.1}
  .name small{font-weight:400;font-size:8px;color:var(--kids)}
  .price{font-size:7px;color:var(--price);white-space:nowrap}
  .desc{font-size:7.2px;line-height:1.18;color:var(--ink)}
  .desc .hint{color:var(--kids)}
  .tag{font-size:6.5px;color:var(--navy);font-weight:600}

  .vegan-box{border:1.5px solid var(--sky);border-radius:8px;padding:3px 4px;text-align:center;margin-top:2px}
  .vegan-box .name{color:var(--alert);font-size:10px}
  .vegan-box .desc{color:var(--alert);font-size:6.5px}
  .gf-note .name{color:var(--alert)}
  .gf-note .desc{color:var(--navy)}

  /* kids panel */
  .kids{position:absolute;left:332px;top:6px;right:2px;bottom:4px;border-left:1px dotted var(--sky);padding:6px 10px}
  .kids-title{font-family:"Playfair Display",Georgia,serif;font-size:17px;color:var(--navy);transform:rotate(-4deg);transform-origin:left;margin-top:8px;letter-spacing:.5px}
  .kids-note{position:absolute;right:14px;top:18px;width:150px;font-family:"Lato",Arial,sans-serif;font-size:5.6px;letter-spacing:.4px;color:var(--navy);transform:rotate(-4deg);text-align:center}
  .kids-list{list-style:none;margin-top:8px}
  .kids-list li{display:flex;justify-content:space-between;font-size:10px;color:var(--kids);padding:3px 0;border-bottom:1px dotted var(--sky-pale)}
  .kids-list li span:last-child{font-size:7px;color:var(--price)}

  /* hours panel */
  .hours{position:absolute;right:0;top:0;width:126px;height:224px;background:var(--sky-pale);display:flex;align-items:center;justify-content:center}
  .hours-ring{width:60px;height:60px;border:2px solid var(--sky);border-radius:50%;display:flex;align-items:center;justify-content:center}
  .hours-ring span{writing-mode:vertical-rl;font-family:"Lato",Arial,sans-serif;font-size:7px;letter-spacing:1px;color:var(--navy);text-align:center}
  .hours-line{position:absolute;left:82px;top:34px;width:2px;height:150px;background:var(--sky)}

  .wheel{position:absolute;width:22px;height:22px;border-radius:50%;background:var(--sky)}
  .wheel-lunch{left:168px;bottom:6px;width:14px;height:14px}
  .wheel-others{left:208px;bottom:8px}
  .base-line{position:absolute;left:130px;bottom:18px;width:190px;height:1px;background:var(--sky)}
</style>
</head>
<body>
<main class="menu">
  <header>
    <div class="brand"><span class="brand-dot"></span><span class="brand-name">The Bramble</span></div>
    <p class="address">14 Hollis Lane, Northvale, tel: 555 0142, www.thebramble.cafe</p>
    <h1 class="title">THE MENU</h1>
  </header>
  <div class="rule rule-top"></div>
  <div class="rule-knot" role="img" aria-label="Rope knot ornament"></div>

  <!-- Breakfast -->
  <section class="section breakfast">
    <div class="side-label"><span class="main">BREAKFAST</span><span class="sub">VEGAN &amp; NON VEGAN</span></div>

    <div class="col" style="left:91px;width:110px">
      <div class="item"><div class="head"><span class="name">Toast <small>buttered</small></span><span class="price">$6.00</span></div>
        <p class="desc"><span class="hint">2 slices:</span> sourdough white or wholemeal, block white or wholemeal, or turkish <span class="hint">Extras:</span> jam, darkspread, honey, peanut butter or cinnamon sugar, or turkish</p></div>
      <div class="item"><div class="head"><span class="name">gf bread (2)</span><span class="price">$8.00</span></div></div>
      <div class="item"><div class="head"><span class="name">turkish raisin</span><span class="price">$6.00</span></div><p class="desc">2 toasts</p></div>
      <div class="item"><div class="head"><span class="name">banana bread</span><span class="price">$5.50</span></div><p class="desc">add whipped mascarpone w/ honey <span class="price">$2.50</span></p></div>
      <div class="item"><div class="head"><span class="name">Granola Muesli</span><span class="price">$11.00</span></div><p class="desc">home made with yoghurt &amp; our own berry compote</p></div>
      <div class="vegan-box"><p class="name">Vegans</p><p class="desc">we are more than happy to make something to suit you</p></div>
    </div>

    <div class="col" style="left:208px;width:227px">
      <div class="item"><div class="head"><span class="name">Spanish Eggs</span><span class="price">$17.00</span></div>
        <p class="desc">two poached range eggs in a warm spanish tomato salsa topped w/ parmesan cheese with toasted sourdough. <span class="hint">w/chorizo</span></p></div>
      <div class="item"><div class="head"><span class="name">Bacon &amp; Eggs</span><span class="price">$16.00</span></div>
        <p class="desc">poached / scrambled or fried) on s/dough toast &amp; side of relish</p></div>
      <div class="item"><div class="head"><span class="name">Bacon &amp; Egg Sandwich</span><span class="price">$12.00</span></div>
        <p class="desc">bacon &amp; egg sandwich turkish bread lightly toasted with (2) bacon, fried egg &amp; your choice of house relish / hollandaise / tom or bbq sauce</p></div>
      <div class="item"><div class="head"><span class="name">Lifestyle Breakfast</span><span class="price">$17.00</span></div>
        <p class="desc">wholemeal sourdough topped with wilted baby spinach, asparagus, mushrooms, two poached eggs w/ grilled tomato &amp; fresh avocado</p></div>
      <div class="item"><div class="head"><span class="name">Eggs Benedict</span><span class="price">$16.50</span></div>
        <p class="desc">toasted sourdough w baby spinach, poached eggs &amp; hollandaise sauce. <span class="hint">w mush $16.5 / w leg ham $16.5 / w bacon $16.5 / w salmon $18.5</span></p></div>
      <div class="item gf-note"><div class="head"><span class="name">Most Items Can Be Made Gluten Free</span><span class="price">$2.00</span></div>
        <p class="desc">chorizo (gf) &nbsp;bacon (gf) &nbsp;ham (gf) &nbsp;relish (gf) &nbsp;hash browns (gf)</p></div>
    </div>

    <div class="col" style="left:442px;width:242px">
      <div class="item"><div class="head"><span class="name">The Big Bramble Breakfast</span><span class="price">$19.00</span></div>
        <p class="desc">toasted sourdough, bacon, eggs (poached, scrambled or fried), chorizo, tomato, mushrooms, baby spinach, hash brown w/ house relish</p></div>
      <div class="item"><div class="head"><span class="name">French Toast</span><span class="price">$16.00</span></div>
        <p class="desc">brioche bread soaked in a creamy cinnamon mix, fried &amp; served with maple syrup, vanilla ice-cream &amp; a side of our berry compote</p></div>
      <div class="item"><div class="head"><span class="name">Pancakes</span><span class="price">$14.00</span></div>
        <p class="desc">two stack of pancakes, topped w maple syrup &amp; ice cream <span class="hint">and grilled bananas $2.00</span></p></div>
      <div class="item"><div class="head"><span class="name">Breakfast Wrap</span><span class="price">$13.00</span></div>
        <p class="desc">bacon, fried egg, spinach, cheese topped with house made relish</p></div>
      <div class="item"><div class="head"><span class="name">Croissants</span><span class="price">$9.00</span></div>
        <p class="desc">ham, cheese &amp; tomato $10.5 / or ham, cheese &amp; avocado $9.5 / w bacon $16.5 / w salmon $18.5</p></div>
      <div class="item"><div class="head"><span class="name">Extras</span><span class="price">$4.00 / $3.00</span></div>
        <p class="desc">ea bacon (2) - egg (2) chorizo - salmon - mushrooms<br>ea grilled tomato - baby spinach (wilted) - avocado<br>hash brown</p></div>
    </div>
  </section>

  <!-- Lunch -->
  <section class="section lunch">
    <div class="side-label"><span class="main">LUNCH</span><span class="sub light">SANDWICHES &amp; ROLLS</span></div>

    <div class="col" style="left:91px;width:110px">
      <div class="item"><div class="head"><span class="name">Chicken Rost</span><span class="price">$14.00</span></div>
        <p class="desc">Marinated chicken breast with tomato, avocado, salad &amp; sweet chilli mayo on toasted turkish bread <span class="tag">GF available</span></p></div>
      <div class="item"><div class="head"><span class="name">The Daisy...</span><span class="price">$14.00</span></div>
        <p class="desc">grilled field mushrooms, haloumi, smashed poached egg, sliced tomato &amp; baby spinach in a toasted tortilla <span class="tag">V</span></p></div>
      <div class="item"><div class="head"><span class="name">The Max....</span><span class="price">$12.00</span></div>
        <p class="desc">house crumbed chicken breast with coleslaw on a toasted roll add bacon (add 2.50)</p></div>
    </div>

    <div class="col" style="left:208px;width:116px">
      <div class="item"><div class="head"><span class="name">Salad Roll...</span><span class="price">$9.00</span></div>
        <p class="desc">tomato, cucumber, avocado, shaved carrot, beetroot, sprouts, alfalfa &amp; mayo... yes you can add to this !! add chicken or ham (add 2.50) <span class="tag">V GF available</span></p></div>
      <div class="item"><div class="head"><span class="name">The Remy...</span><span class="price">$14.00</span></div>
        <p class="desc">pulled bbq hickory smoked beef brisket, fried egg, bacon, sliced tomato &amp; lettuce on a soft roll</p></div>
      <div class="item"><div class="head"><span class="name">Bleat...</span><span class="price">$12.00</span></div>
        <p class="desc">grilled bacon, lettuce, egg, avocado &amp; tomato with mayo in a toasted tortilla <span class="tag">GF</span></p></div>
    </div>

    <div class="kids">
      <h2 class="kids-title">KIDS ALL DAY MEALS</h2>
      <p class="kids-note">THESE ARE KIDS MEALS. IF YOU CAN SEE OVER THE COUNTER, DON'T EVEN BOTHER</p>
      <ul class="kids-list">
        <li><span>Fairy Bread</span><span>4.00</span></li>
        <li><span>Boiled Eggs With Toast Soldiers</span><span>8.00</span></li>
        <li><span>Grilled Cheesy Darkspread Fingers</span><span>6.00</span></li>
        <li><span>Mini Ham &amp; Cheese Or Pineapple &amp; Cheese Pizza</span><span>8.00</span></li>
        <li><span>Crumbed Chicken Fingers With Factory Frites</span><span>8.50</span></li>
        <li><span>Chocolate or Strawberry Flavoured Milk</span><span>4.50</span></li>
      </ul>
    </div>
    <div class="wheel wheel-lunch" role="img" aria-label="Ship's wheel ornament"></div>
  </section>

  <!-- The Others -->
  <section class="section others">
    <div class="side-label"><span class="sub light">THE OTHERS</span></div>

    <div class="col" style="left:91px;width:226px">
      <div class="item"><div class="head"><span class="name">Famous Factory Beef &amp; Red Wine Pie</span><span class="price">$16.00</span></div>
        <p class="desc">served with garden salad</p></div>
      <div class="item"><div class="head"><span class="name">Roasters Board...</span><span class="price">$16.00</span></div>
        <p class="desc">toasted flat bread, dip &amp; chutney, relish, pickled vegetables, haloumi, Marinated local olives shaved Serrano ham &amp; poached chicken <span class="tag">V GF</span></p></div>
      <div class="item"><div class="head"><span class="name">Tuna &amp; Baby Cos Salad</span><span class="price">$18.00</span></div>
        <p class="desc">seared pistachio, lemon, parmesan &amp; caper crusted tuna, baby cos lettuce &amp; pomegranate salad, greens &amp; roasted garlic vinaigrette</p></div>
      <div class="item"><div class="head"><span class="name">Toast</span><span class="price">$6.00</span></div>
        <p class="desc">choice of sourdough, turkish or gluten free bread with butter &amp; either housemade preserves, darkspread, peanut butter or ricotta &amp; honeycomb. <span class="tag">GF</span></p></div>
    </div>

    <div class="col" style="left:325px;width:232px">
      <div class="item"><div class="head"><span class="name">Spinach Ricotta, Pinenut &amp; Sweet Potato Filo Pastry Pie</span><span class="price">$16.00</span></div>
        <p class="desc">with salad &amp; tzatziki <span class="tag">V</span></p></div>
      <div class="item"><div class="head"><span class="name">The Son In Law Salad</span><span class="price">$18.00</span></div>
        <p class="desc">shredded asian greens &amp; rice noodles tossed with toasted peanuts &amp; served with son in law eggs &amp; a tamarind molasses dressing <span class="tag">V GF</span></p></div>
      <div class="item"><div class="head"><span class="name">Poached Chicken &amp; Asparagus Salad</span><span class="price">$18.00</span></div>
        <p class="desc">with tarragon poached chicken &amp; grilled asparagus, kipfler potato &amp; cress with a tomato &amp; tahini dressing <span class="tag">GF</span></p></div>
      <div class="item"><div class="head"><span class="name">Breakfast Plate</span><span class="price">$17.50</span></div>
        <p class="desc">toasted flat bread with fresh ricotta, sliced tomato, fresh basil, roasted pepper &amp; eggplant babaghanoush, sliced avocado &amp; a soft poached egg..add on extras from list on the right <span class="tag">GF</span></p></div>
    </div>

    <aside class="hours">
      <div class="hours-line"></div>
      <div class="hours-ring"><span>OPEN<br>7AM<br>3PM</span></div>
    </aside>
    <div class="base-line"></div>
    <div class="wheel wheel-others" role="img" aria-label="Ship's wheel ornament"></div>
  </section>
</main>
</body>
</html>
```